Verdell Chiropractic, achieve your health goals, get better each day one step at a time

A mobile friendly site, fresh look, easy to navigate, has interface with pw/chirply, etc. Blog posts. Uses new logo. Content and address to current site is mirvaton.com. The current site will give you scope of project for content. The logo is not the final but close. Will upload final next week.
Convey the concept that heath is a process, it does not just happen. We take steps to achieve what we want in life including health.

Target Market(s)

30 to 70 year old. Needing health care

Industry/Entity Type

Health Care

Coding

Coded - Design and coding required

Number of Pages Required

5+ page

Font styles to use
Sans Serif

Colors

Designer to choose colors to be used in the design.

Requirements
Must have
• mobile friendly, easy to navigate, PW/Chirply interface, blog, room for current content
Nice to have
• potential for commerce, statistics
Should not have
• Same old look and feel as everything else out there

```html
<!DOCTYPE html>
<html lang="en">
<head>
<meta charset="utf-8">
<title>Verdell Chiropractic</title>
<link href="https://fonts.googleapis.com/css2?family=Josefin+Sans:wght@400;600;700&family=EB+Garamond:wght@400;600;700&display=swap" rel="stylesheet">
<style>
  :root {
    --white: #ffffff;
    --ink: #3a3a3a;
    --body-text: #4a4a4a;
    --navy: #1f3447;
    --brand: #1f5d6b;
    --hero-dark: #6a3a10;
    --hero-mid: #c7771e;
    --hero-light: #f5c04a;
    --gold: #e8b21a;
    --headline: #5a2e0c;
    --sand: #e4d9d4;
    --footer: #6b5142;
    --method-top: #8fa3a3;
    --method-bottom: #7a6e66;
  }
  * { box-sizing: border-box; margin: 0; padding: 0; }
  html, body { width: 1200px; height: 2586px; overflow: hidden; background: var(--white); }
  body { position: relative; font-family: "EB Garamond", Georgia, serif; color: var(--body-text); }
  .abs { position: absolute; }
  .sans { font-family: "Josefin Sans", Arial, sans-serif; }

  /* Hero */
  .hero { left: 0; top: 0; width: 1200px; height: 707px; overflow: hidden;
    background: radial-gradient(ellipse at 40% 45%, var(--hero-light) 0%, var(--hero-mid) 35%, var(--hero-dark) 100%); }
  .hero-art { left: 60px; top: 160px; width: 720px; height: 470px;
    background: radial-gradient(ellipse at center, rgba(255,230,140,.85) 0%, rgba(230,150,40,.5) 45%, rgba(120,60,10,0) 75%); }
  .hero-wave { left: 0; top: 590px; width: 1200px; height: 117px; }
  .hero-title { left: 514px; top: 240px; font-size: 53px; color: var(--headline); letter-spacing: .5px; white-space: nowrap; }
  .hero-sub { left: 898px; top: 322px; font-size: 21px; line-height: 28px; color: var(--headline); letter-spacing: 1.5px; white-space: nowrap; }

  /* Header */
  .site-header { left: 0; top: 0; width: 1200px; height: 107px; background: rgba(225,225,225,.72); }
  .brand-name { left: 103px; top: 36px; font-size: 34px; font-weight: 700; color: var(--brand); white-space: nowrap; }
  .main-nav { right: 56px; top: 46px; display: flex; gap: 34px; list-style: none; }
  .main-nav li { font-size: 22px; color: var(--white); letter-spacing: .5px; }

  /* Reliable care */
  .care-title { left: 98px; top: 752px; font-size: 42px; color: var(--ink); }
  .copy { font-size: 19px; line-height: 27px; }
  .care-copy { left: 98px; top: 826px; width: 350px; }
  .care-sub { left: 100px; top: 1093px; font-size: 23px; color: var(--ink); letter-spacing: 1px; }
  .care-note { left: 107px; top: 1146px; width: 300px; }
  .care-photo { left: 534px; top: 748px; width: 642px; height: 454px;
    background: linear-gradient(120deg, #eef0f2 0%, #d9dde0 45%, #c9a894 70%, #e9e9ea 100%);
    box-shadow: 0 3px 10px rgba(0,0,0,.3); }

  /* Method */
  .method { left: 0; top: 1272px; width: 1200px; height: 445px;
    background: linear-gradient(180deg, var(--method-top) 0%, #a69a92 45%, var(--method-bottom) 100%); }
  .method-title { left: 0; top: 1443px; width: 1148px; text-align: center; font-size: 32px; color: var(--white); letter-spacing: 1.5px; }
  .method-copy { left: 264px; top: 1510px; width: 700px; color: var(--white); }

  /* Features */
  .features { left: 0; top: 1717px; width: 1200px; height: 552px; background: var(--sand); }
  .feat-title { left: 88px; top: 1770px; font-size: 39px; color: var(--navy); letter-spacing: 1px; }
  .feat-head { font-size: 23px; color: var(--navy); letter-spacing: 1px; }
  .feat-copy { font-size: 17.5px; line-height: 25px; color: #5e5650; }
  .feat-photo { left: 624px; top: 1969px; width: 507px; height: 234px;
    background: linear-gradient(110deg, #e9e7e6 0%, #d8b9a6 45%, #e6c7b3 70%, #dcdcdc 100%); }

  /* Footer */
  .site-footer { left: 0; top: 2269px; width: 1200px; height: 317px; background: var(--footer); color: var(--white); }
  .foot-head { font-size: 17px; font-weight: 700; letter-spacing: 1px; color: var(--white); }
  .foot-list { list-style: none; font-size: 14px; font-weight: 700; line-height: 22.5px; color: var(--white); }
  .foot-text { font-size: 14px; font-weight: 700; line-height: 22px; color: var(--white); }
  .foot-more { font-size: 11px; font-weight: 700; letter-spacing: .5px; color: var(--white); }
</style>
</head>
<body>

<section class="hero abs">
  <div class="hero-art abs" role="img" aria-label="Glowing silhouette of a human torso with golden orbit rings around the spine"></div>
  <svg class="hero-wave abs" viewBox="0 0 1200 117" preserveAspectRatio="none">
    <path d="M0 40 C300 0 700 10 1200 50 L1200 117 L0 117 Z" fill="#f0c030"/>
    <path d="M0 70 C350 35 750 45 1200 75 L1200 117 L0 117 Z" fill="var(--gold)"/>
  </svg>
  <h1 class="hero-title abs sans" style="font-weight:400">Achieve your health goals</h1>
  <p class="hero-sub abs sans">GET BETER EACH DAY<br>ONE STEP AT A TIME</p>
</section>

<header class="site-header abs">
  <div class="brand-name abs sans">Verdell Chiropractic</div>
  <ul class="main-nav abs sans">
    <li>HOME</li><li>SERVICES</li><li>PORTFOLIO</li><li>ABOUT</li><li>CONTACT</li>
  </ul>
</header>

<section>
  <h2 class="care-title abs sans" style="font-weight:400">Reliable Care</h2>
  <p class="care-copy copy abs">Donec pretium mattis augue vel bibendum. Mauris non nibh in tortor placerat pharetra. Nunc ut lacinia elit. Mauris nec ante ac quam dictum suscipit. Sed orci quam, fringilla vitae semper at, venenatis vel tellus. Suspendisse lacinia laoreet turpis et blandit. Pellentesque habitant morbi tristique senectus et netus</p>
  <h3 class="care-sub abs sans" style="font-weight:400">ET PERQUE SUT</h3>
  <p class="care-note copy abs">Lorem ipsum dolor sit amet, consectetur adipiscing elit.</p>
  <div class="care-photo abs" role="img" aria-label="Therapist's hands supporting the neck of a woman lying on a treatment table"></div>
</section>

<section>
  <div class="method abs" role="img" aria-label="Close-up of a bare back with a flowering branch laid across it"></div>
  <h2 class="method-title abs sans" style="font-weight:400">OUR METHOD</h2>
  <p class="method-copy copy abs">Donec pretium mattis augue vel bibendum. Mauris non nibh in tortor placerat pharetra. Nunc ut lacinia elit. Mauris nec ante ac quam dictum suscipit. Sed orci quam, fringilla vitae semper at, venenatis vel tellus. Suspendisse lacinia laoreet turpis et blandit. Pellentesque habitant morbi tristique senectus et netus et malesuada fames ac turpis egestas.</p>
</section>

<section>
  <div class="features abs"></div>
  <h2 class="feat-title abs sans" style="font-weight:400">ETIAM AT QUOQUE</h2>
  <p class="feat-copy abs" style="left:88px;top:1830px;width:495px">Quisque tincidunt quam a porta sagittis. Etiam at urna dolor. Curabitur semper, arcu ut consequat sagittis, arcu purus venenatis est, et tristique nibh nibh porttitor odio. Nunc blandit ac ante in accumsan. Vestibulum ac tincidunt eros. Suspendisse elementum in nisi ut fringilla. Suspendisse tincidunt orci sit amet tellus porta</p>
  <h3 class="feat-head abs sans" style="left:88px;top:1986px;font-weight:400">ET QUIQUE POTEST</h3>
  <p class="feat-copy abs" style="left:88px;top:2040px;width:495px">Quisque tincidunt quam a porta sagittis. Etiam at urna dolor. Curabitur semper, arcu ut consequat sagittis, arcu purus venenatis est, et tristique nibh nibh porttitor odio. Nunc blandit ac ante in</p>
  <h3 class="feat-head abs sans" style="left:626px;top:1781px;font-weight:400">PERPIT PERLEXA</h3>
  <p class="feat-copy abs" style="left:626px;top:1817px;width:500px">Quisque tincidunt quam a porta sagittis. Etiam at urna dolor. Curabitur semper, arcu ut consequat sagittis, arcu purus venenatis est, et tristique nibh nibh porttitor odio. Nunc blandit ac ante in</p>
  <h4 class="abs sans" style="left:626px;top:1914px;font-size:17px;font-weight:400;color:var(--navy);letter-spacing:.5px">ETERNITATEM MAGISTIMA CHOSE</h4>
  <div class="feat-photo abs" role="img" aria-label="Hands massaging a foot"></div>
</section>

<footer class="site-footer abs">
  <h4 class="foot-head abs sans" style="left:100px;top:88px">OUR LOCATION</h4>
  <p class="foot-text abs" style="left:100px;top:146px;line-height:33px">Lipsum quoque 10, et per<br>23, perque, Et sit</p>
  <p class="foot-more abs" style="left:100px;top:240px">SEE ON MAPS</p>

  <h4 class="foot-head abs sans" style="left:464px;top:88px">LINKS</h4>
  <ul class="foot-list abs" style="left:461px;top:130px">
    <li>HOME</li><li>PORTFOLIO</li><li>SERVICES</li><li>ABOUT</li><li>CONTACT</li>
  </ul>

  <h4 class="foot-head abs sans" style="left:641px;top:88px">ABOUT US</h4>
  <p class="foot-text abs" style="left:641px;top:146px;width:225px">Suspendisse aliquet purus et lectus consequat, vel auctor ante auctor. Nam et sapien</p>
  <p class="foot-more abs" style="left:643px;top:238px">READ MORE</p>

  <h4 class="foot-head abs sans" style="left:998px;top:88px">COMPANY</h4>
  <ul class="foot-list abs" style="left:997px;top:130px">
    <li>PHARETRA</li><li>ECIT</li><li>PERQUE</li><li>ED SAE</li><li>QUOQUE</li>
  </ul>
</footer>

</body>
</html>
```